Awesome, colorful pamphlet advertising services for disabled people and supporters

My business, The Wellness Crossroads, provides nutritional counseling services to people with and without disabilities throughout the lifespan. It also offers disability consulting, body image coaching and accessible recreation consultation. I would like something representing both children and adults which ties these activities together in a happy way.

Font styles to use
Sans Serif

Colors
00AB8E
00BBA5
67D7C9
C6EFE9
E9F9F6
FFF300
FFF600
FEFA6F
FFFEC7
FFFEE8
F0912C
F2A743
F7CA91
FBE8D2
FDF5EE
E54698
E96AAD
F1A4CE
F9D9EA
FCEFF6
6B429C
8869AF
B7A5CE
E3DAEB
F3F0F8

```html
<!DOCTYPE html>
<html lang="en">
<head>
<meta charset="utf-8">
<title>The Wellness Crossroads – Pamphlet</title>
<link href="https://fonts.googleapis.com/css2?family=Oswald:wght@300;400&family=Lobster&family=Montserrat:wght@400;600;700&display=swap" rel="stylesheet">
<style>
:root{
  --board:#2b2b2b;
  --purple:#8a5c92;
  --purple-deep:#6b429c;
  --purple-soft:#b7a5ce;
  --pink:#e6176f;
  --pink-soft:#e96aad;
  --grey:#e4e4e6;
  --grey-light:#f2f2f3;
  --ink:#222222;
  --white:#ffffff;
}
*{margin:0;padding:0;box-sizing:border-box}
html,body{width:834px;height:1200px;overflow:hidden;background:var(--board)}
body{position:relative;font-family:"Montserrat",Arial,sans-serif;color:var(--ink)}
.page{position:absolute;background:var(--white);overflow:hidden}
.page svg.bg{position:absolute;left:0;top:0}
.page-bio{left:42px;top:103px;width:362px;height:477px;background:linear-gradient(#ececee,#f7f7f8)}
.page-cover{left:417px;top:103px;width:371px;height:477px}
.page-org{left:42px;top:605px;width:362px;height:477px}
.page-services{left:417px;top:605px;width:371px;height:477px}
.abs{position:absolute}
.script{font-family:"Lobster",cursive}
.condensed{font-family:"Oswald",Arial Narrow,sans-serif;font-weight:300;letter-spacing:.5px}

/* bio page */
.portrait{left:22px;top:19px;width:102px;height:102px;border-radius:50%;border:5px solid var(--white);box-shadow:0 0 0 3px var(--pink);background:radial-gradient(circle at 50% 40%,#9c7e74,#5d4a48 70%,#3b3234)}
.bio-name{left:140px;top:22px;color:var(--white);font-size:20px}
.bio-cred{left:140px;top:48px;color:var(--white);font-size:9.5px;font-weight:600}
.bio-text{left:19px;top:137px;width:322px;font-size:5.6px;line-height:7.1px;text-align:justify}
.bio-text p{margin-bottom:6px}
.badge{top:292px;width:64px;height:64px;border-radius:50%}
.badge-a{left:25px;background:var(--purple);box-shadow:0 0 0 3px #fff inset}
.badge-b{left:97px;background:#fff;border:5px solid var(--pink)}
.badge-c{left:172px;background:#fff;border:5px solid var(--purple)}
.contact-title{left:34px;top:410px;color:var(--purple);font-size:14px}
.contact-lines{left:36px;top:430px;font-size:6.5px;line-height:8.2px;font-weight:600}
.contact-lines .who{color:var(--pink);font-weight:700}
.bio-url{right:18px;top:427px;color:var(--purple);font-size:12.5px;font-weight:700}
.bio-social{right:18px;top:446px;color:var(--pink);font-size:8px;font-weight:700}

/* cover page */
.cover-title{left:18px;top:328px;font-size:45px;line-height:47px;color:var(--purple)}
.cover-title .second{color:var(--pink)}
.cover-url{right:16px;top:454px;color:var(--white);font-size:10px;font-weight:700}
.cover-globe{right:27px;top:432px}

/* organisations page */
.org-title{left:20px;top:20px;color:var(--white);font-size:40px;line-height:40px;font-weight:400}
.section-head{font-size:9px;font-weight:700}
.section-head .accent{color:var(--pink)}
.org-head{left:24px;top:149px}
.bullets{list-style:none}
.bullets li{position:relative;padding-left:10px}
.bullets li::before{content:"";position:absolute;left:0;top:50%;margin-top:-3px;border-left:5px solid var(--pink);border-top:3px solid transparent;border-bottom:3px solid transparent}
.org-list{left:25px;top:165px;font-size:7.3px;line-height:16px}
.pres-title{left:19px;top:282px;color:var(--purple);font-size:26px;font-weight:400}
.pres-intro{left:20px;top:312px;font-size:5.8px}
.pres-list{left:20px;top:329px;font-size:5.6px;line-height:11.3px;text-transform:uppercase}
.pres-list li::before{margin-top:-2.5px;border-left-width:4px;border-top-width:2.5px;border-bottom-width:2.5px}

/* services page */
.svc-title{left:20px;top:24px;color:var(--white);font-size:19px}
.svc-head{left:28px;top:112px;font-size:9.5px;line-height:12px}
.svc-intro{left:28px;top:148px;font-size:5.8px}
.svc-list{left:28px;top:161px;font-size:6.3px;line-height:13.6px}
.future{left:232px;top:262px;width:130px;height:205px;background:var(--purple);padding:10px 8px}
.future-head{display:block;border:1.5px solid var(--white);background:var(--pink);color:var(--white);font-size:9.5px;font-weight:700;text-align:center;padding:3px 0;margin-bottom:9px}
.future-list{color:var(--white);font-size:5.6px;line-height:7px}
.future-list li{margin-bottom:8px}
.future-list li::before{border-left-color:var(--white);top:3.5px;margin-top:0;border-left-width:4px;border-top-width:2.5px;border-bottom-width:2.5px}
</style>
</head>
<body>

<!-- Bio page -->
<section class="page page-bio">
  <svg class="bg" width="362" height="477" viewBox="0 0 362 477">
    <path d="M0 0H362V18C330 95 230 110 110 112L0 108Z" fill="var(--purple)"/>
    <path d="M110 112C230 110 330 95 362 18V34C335 105 240 122 110 118Z" fill="var(--pink)"/>
    <path d="M0 365C80 395 190 400 262 372C200 410 90 415 0 392Z" fill="var(--pink)"/>
    <path d="M0 392C90 415 200 410 262 372C230 430 120 440 0 420Z" fill="#d9d9dc"/>
    <path d="M0 400C120 440 260 430 362 370V477H0Z" fill="var(--white)"/>
  </svg>
  <div class="abs portrait" role="img" aria-label="Portrait photo of the counselor"></div>
  <div class="abs bio-name script">Dana Whitfield</div>
  <div class="abs bio-cred">MSW, CARSS I,CFNC</div>
  <div class="abs bio-text">
    <p>Dana Whitfield has been passionate about disability issues since 2003 when she discovered disability rights and the disability activism community. This changed her life and helped her feel stronger about herself, her disabilities, and her capabilities. In 2011, she became sick with Postural Orthostatic Tachycardia Syndrome. This was severe and life changing. It taught her about the overlap of disability and chronic illness in a way that nothing but experience can. It has been quite a journey to live with and manage. As a result, she cares about people with POTS and the wider chronic illness community and is now a certified nutrition counselor with a chronic illness emphasis.</p>
    <p>She also holds a Melodygarden early childhood music and movement teacher license for babies through age seven, certification as an Adaptive Recreation and Sports Specialist from Summit Adaptive Sports and CircleChat for seniors group facilitator certification. Lastly, she earned certificates in both working with veterans and their families from Lakeshore State University and a Trauma Informed Clinical Foundation Certificate from Northfield University. Because she cares about trauma and body image, she is also a certified body image coach for people with and without disabilities/illness.</p>
    <p>While varied, each of these has been carefully chosen for its philosophies and contributions to The Wellness Crossroads when combined with our framework.</p>
  </div>
  <div class="abs badge badge-a" role="img" aria-label="Certification badge"></div>
  <div class="abs badge badge-b" role="img" aria-label="Certification badge"></div>
  <div class="abs badge badge-c" role="img" aria-label="Certification badge"></div>
  <div class="abs contact-title script">Contact Us</div>
  <div class="abs contact-lines">
    <div class="who">DANA WHITFIELD</div>
    <div>Phone Number</div>
    <div>Email</div>
    <div>Address</div>
  </div>
  <div class="abs bio-url">wellnesscrossroads.org</div>
  <div class="abs bio-social">@wellnesscrossroads</div>
</section>

<!-- Cover page -->
<section class="page page-cover">
  <svg class="bg" width="371" height="477" viewBox="0 0 371 477">
    <defs>
      <linearGradient id="kids" x1="0" y1="0" x2="1" y2="1">
        <stop offset="0" stop-color="#c9c25a"/><stop offset=".5" stop-color="#e9b7a0"/><stop offset="1" stop-color="#d78b6e"/>
      </linearGradient>
      <linearGradient id="seniors" x1="0" y1="0" x2="1" y2="1">
        <stop offset="0" stop-color="#8fae5c"/><stop offset=".6" stop-color="#d7b7a3"/><stop offset="1" stop-color="#b8463c"/>
      </linearGradient>
    </defs>
    <path d="M0 0H371V80C330 200 200 280 0 260Z" fill="url(#kids)" role="img" aria-label="Photo of a group of laughing children"/>
    <path d="M0 260C200 280 330 200 371 80V105C320 230 210 300 0 300Z" fill="var(--purple)"/>
    <path d="M0 285C210 290 330 215 371 110V120C320 245 200 300 0 300Z" fill="var(--pink)"/>
    <path d="M371 220V440C320 445 250 455 200 460C270 400 220 310 170 300C260 290 330 250 371 220Z" fill="url(#seniors)" role="img" aria-label="Photo of a joyful older couple outdoors"/>
    <path d="M210 477C260 440 320 425 371 422V477Z" fill="var(--purple)"/>
    <path d="M210 477C255 438 320 420 371 418V424C320 428 262 444 222 477Z" fill="var(--pink)"/>
  </svg>
  <h1 class="abs cover-title condensed">WELLNESS<br><span class="second">CROSSROADS</span></h1>
  <svg class="abs cover-globe" width="16" height="16" viewBox="0 0 16 16" fill="none" stroke="#fff" stroke-width="1.2">
    <circle cx="8" cy="8" r="7"/><ellipse cx="8" cy="8" rx="3" ry="7"/><path d="M1 8H15M2.5 4.5H13.5M2.5 11.5H13.5"/>
  </svg>
  <div class="abs cover-url">wellnesscrossroads.org</div>
</section>

<!-- Organisations page -->
<section class="page page-org">
  <svg class="bg" width="362" height="477" viewBox="0 0 362 477">
    <defs>
      <linearGradient id="hands" x1="0" y1="0" x2="1" y2="0">
        <stop offset="0" stop-color="#e6176f" stop-opacity="0"/><stop offset=".5" stop-color="#b8607f"/><stop offset="1" stop-color="#6a4060"/>
      </linearGradient>
    </defs>
    <path d="M0 0H362V130C250 115 120 120 0 145Z" fill="var(--pink)"/>
    <path d="M150 0H362V130C300 120 220 118 150 124Z" fill="url(#hands)" role="img" aria-label="Photo of two hands clasped together"/>
    <path d="M0 260C120 240 260 250 362 275V477H0Z" fill="var(--grey)"/>
  </svg>
  <h2 class="abs org-title condensed">LETS WORK<br>TOGETHER</h2>
  <h3 class="abs section-head org-head">SERVICES FOR <span class="accent">ORGANIZATIONS</span></h3>
  <ul class="abs bullets org-list">
    <li>Program Development and Growth Support</li>
    <li>Customized Presentations/Workshops for Staff Development</li>
    <li>Curriculum and Resource Creation Services Based on Your Goals</li>
    <li>Articles, Blog Posts and Other Content on Commission</li>
    <li>Handmade Collage Art and Creative Writing Pieces for your Office/Program</li>
  </ul>
  <h2 class="abs pres-title condensed">PRESENTATION</h2>
  <p class="abs pres-intro">Dana is currently presenting these topics- Contact for Customized Presentation for your Organization</p>
  <ul class="abs bullets pres-list">
    <li>Disability history and culture</li>
    <li>Body esteem and eating disorders as a disability issue</li>
    <li>How to build self-definition and self-compassion</li>
    <li>Trauma and disability: what to know and what to do</li>
    <li>Lessons from disability history:</li>
    <li>How to embrace our community's darkest times to create change and healing</li>
    <li>Patient lifts:</li>
    <li>What to know and how to incorporate them in a way that works for disabled people</li>
    <li>We are strong:</li>
    <li>Program development from a disability rights perspective</li>
    <li>Trauma response:</li>
    <li>Helping people ground themselves, stabilize, and recover</li>
  </ul>
</section>

<!-- Services page -->
<section class="page page-services">
  <svg class="bg" width="371" height="477" viewBox="0 0 371 477">
    <defs>
      <linearGradient id="friends" x1="0" y1="0" x2="1" y2="1">
        <stop offset="0" stop-color="#e8ecea"/><stop offset=".4" stop-color="#a8b78a"/><stop offset="1" stop-color="#5e6f8a"/>
      </linearGradient>
      <linearGradient id="family" x1="0" y1="0" x2="1" y2="1">
        <stop offset="0" stop-color="#f1e9e2"/><stop offset=".35" stop-color="#d39b6a"/><stop offset=".75" stop-color="#8a5a3a"/><stop offset="1" stop-color="#5b4a48"/>
      </linearGradient>
    </defs>
    <rect x="0" y="0" width="371" height="110" fill="var(--grey)"/>
    <path d="M180 0H371V105C310 92 250 88 180 88Z" fill="url(#friends)" role="img" aria-label="Photo of four friends sitting together on grass"/>
    <path d="M0 0H165C145 55 80 85 0 92Z" fill="var(--purple)"/>
    <path d="M0 92C80 85 145 55 165 0H172C150 62 90 95 0 100Z" fill="var(--white)"/>
    <path d="M0 110C120 88 270 85 371 110V138C280 110 150 105 0 118Z" fill="var(--pink)"/>
    <path d="M0 118C150 105 280 110 371 138V477H0Z" fill="var(--white)"/>
    <path d="M0 300C80 292 170 296 240 300V477H0Z" fill="url(#family)" role="img" aria-label="Photo of a smiling family with a father in a wheelchair, a child and a puppy"/>
  </svg>
  <h2 class="abs svc-title script">Services</h2>
  <h3 class="abs section-head svc-head">CURRENT SERVICES FOR<br><span class="accent">INDIVIDUALS/FAMILIES/SMALL GROUPS</span></h3>
  <p class="abs svc-intro">Dana is currently providing non-clinical assistance for the following:</p>
  <ul class="abs bullets svc-list">
    <li>Self and Body esteem as related to disability</li>
    <li>Trauma and healing with a disability</li>
    <li>Early childhood support for disabled children and care providers</li>
    <li>General disability issues/peer level support</li>
    <li>Movement as fun for disabled kids and adults</li>
    <li>Moving away from therapies / assessing therapy from a disability positive perspective</li>
    <li>Accessible Recreation/Play Cons</li>
  </ul>
  <aside class="abs future">
    <span class="future-head">FUTURE SERVICES</span>
    <ul class="bullets future-list">
      <li>CircleChat senior socialization groups</li>
      <li>Melodygarden early childhood music and movement classes for infants &amp; children up to age 7</li>
      <li>Functional nutrition consultation</li>
      <li>Consultation for people with chronic illnesses such as Postural Orthostatic Tachycardia Syndrome (POTS) and Neurocardiogenic Syncope</li>
      <li>Play Groups</li>
      <li>Classes and social groups for teenagers</li>
      <li>Social groups for veterans</li>
    </ul>
  </aside>
</section>

</body>
</html>
```